Web Design Project

We have a website in beta that needs updating and are looking for a freash new look for the Home page including Logo.
Our company is called " Pim Sa Ox " we specialize in classified advertising using video. Our consumers will be businesses selling a product or service. Please visit www.pimsaox.com
Our aim past this point is to engage a developer to write the code based on the best design. Our target market is the U.S and I have included some of the landing pages to give you a better idea of what we are trying to acheive

http://www.pimsaox.com/
http://www.pimsaox.com/cars_home.php
http://www.pimsaox.com/boats.php
http://www.pimsaox.com/electronic.php
http://www.pimsaox.com/realestate.php
http://www.pimsaox.com/roommates.php

Target Market(s)

20-35 yr old people who are connected to the internet via mobile phone and use social media on a daily/weekly basis

Industry/Entity Type

Advertising

Requirements
Must have
• We would like to use lots of images to convey it is a video driven website business
Nice to have
• Logo to incorporate same theme of website ( ie ) you are here to watch videos of thinhs to buy & sell
Should not have
• This is to be a freash new site with large type and bold fonts

```html
<!DOCTYPE html>
<html lang="en">
<head>
<meta charset="utf-8">
<title>Pim Sa Ox — #1 Video Classifieds</title>
<link href="https://fonts.googleapis.com/css2?family=Open+Sans:wght@400;600;700&family=Raleway:wght@300;400&display=swap" rel="stylesheet">
<style>
:root{
  --navy:#0d4a86;
  --navy-dark:#083a6e;
  --blue-btn:#0b4f8d;
  --orange:#e2461b;
  --orange-soft:#e8532a;
  --grey-dark:#4a4a4a;
  --footer-bg:#f1f1f1;
  --line:#dcdcdc;
  --white:#ffffff;
}
*{box-sizing:border-box;margin:0;padding:0}
html,body{width:863px;height:1200px;overflow:hidden;background:var(--white)}
body{position:relative;font-family:"Open Sans",Arial,sans-serif;color:var(--grey-dark)}
a{text-decoration:none;color:inherit}

.top-strip{position:absolute;top:0;left:0;width:863px;height:6px;background:var(--navy)}
.site-header{position:absolute;top:6px;left:0;width:863px;height:94px;background:linear-gradient(#fff,#f2f2f2)}
.brand{position:absolute;left:102px;top:12px;display:flex;align-items:center;gap:8px}
.brand-dot{width:30px;height:30px;border-radius:50%;background:var(--orange)}
.brand-name{font-size:25px;font-weight:700;color:var(--grey-dark)}
.brand-claim{position:absolute;left:103px;top:62px;font-size:16px;font-weight:700;color:var(--grey-dark)}
.btn{position:absolute;top:7px;height:24px;border-radius:4px;color:#fff;font-size:11px;font-weight:700;display:flex;align-items:center;justify-content:center}
.btn-create{left:611px;width:87px;background:var(--blue-btn)}
.btn-signin{left:701px;width:61px;background:var(--orange)}
.search{position:absolute;left:611px;top:38px;width:151px;height:21px;border:1px solid #d8d8d8;border-radius:3px;background:#fff;font-size:9px;color:#999;padding:4px 7px}
.search-go{position:absolute;right:1px;top:1px;width:19px;height:17px;background:#2a9fd8;color:#fff;font-size:9px;font-weight:700;border-radius:2px;display:flex;align-items:center;justify-content:center}
.lang{position:absolute;left:697px;top:66px;width:64px;height:20px;border:1px solid #e2e2e2;border-radius:3px;background:#fff;font-size:10px;color:var(--navy);padding:3px 7px}
.lang::after{content:"";position:absolute;right:8px;top:7px;border:5px solid transparent;border-top:6px solid var(--navy)}

.main-nav{position:absolute;top:100px;left:0;width:863px;height:53px;background:linear-gradient(var(--navy),var(--navy-dark))}
.nav-bar{position:absolute;left:101px;top:26px;width:661px;height:24px;border-radius:4px;background:linear-gradient(#f4f4f4,#cfcfcf);display:flex}
.nav-item{position:relative;height:24px;display:flex;align-items:center;justify-content:center;font-size:11.5px;font-weight:600;color:#3c3c3c;border-right:1px solid #b9b9b9}
.nav-item:last-child{border-right:0}
.nav-icon{position:absolute;top:-24px;left:50%;transform:translateX(-50%)}

.hero{position:absolute;top:153px;left:0;width:863px;height:373px;overflow:hidden}
.hero-media{position:absolute;inset:0;background:linear-gradient(170deg,#3f7cc8 0%,#a9c7e8 12%,#eef3f8 24%,#ffffff 38%,#e4e9ee 48%,#2a2d33 58%,#1d2025 64%,#eef1f4 72%,#3d6a9d 80%,#1f4577 100%)}
.play{position:absolute;left:386px;top:142px}
.slider-dots{position:absolute;left:362px;top:510px;display:flex;gap:2px}
.slider-dots span{width:33px;height:3px;background:rgba(255,255,255,.6)}
.slider-dots span.active{background:var(--orange)}

.featured{position:absolute;top:540px;left:101px;width:661px}
.featured-kicker{font-family:"Raleway",sans-serif;font-size:16px;color:var(--grey-dark)}
.featured-title{font-size:18px;font-weight:700;color:var(--orange);margin-top:-3px}
.tabs{position:absolute;right:0;top:11px;display:flex;gap:3px}
.tab{height:28px;display:flex;align-items:center;justify-content:center;font-family:"Raleway",sans-serif;font-size:13px;color:#fff;background:var(--blue-btn);border-radius:3px 3px 0 0}
.tab.active{background:var(--orange-soft)}
.featured-rule{position:absolute;left:0;top:39px;width:661px;height:1px;background:var(--line)}
.thumbs{position:absolute;top:48px;left:0;display:flex;gap:5px}
.thumb{width:106px;height:105px}

.how{position:absolute;top:725px;left:0;width:863px}
.how-rule{position:absolute;top:10px;left:0;width:863px;height:1px;background:var(--line)}
.how-title{position:absolute;left:333px;top:-4px;width:192px;text-align:center;background:#fff;font-family:"Raleway",sans-serif;font-weight:300;font-size:24px;color:var(--orange)}
.steps{position:absolute;left:0;top:0}
.step-label{position:absolute;width:170px;text-align:center;font-family:"Raleway",sans-serif;font-weight:300;font-size:21px;color:#777;top:232px}
.step-label::after{content:"";display:block;width:60px;height:3px;background:var(--orange);margin:6px auto 0}

.site-footer{position:absolute;top:1027px;left:0;width:863px;height:173px;background:var(--footer-bg);border-top:2px solid #d4d4d4}
.foot-col{position:absolute;top:10px}
.foot-col h4{font-size:11.5px;font-weight:700;color:var(--grey-dark);margin-bottom:6px}
.foot-col li{list-style:none;font-size:10.5px;color:#777;line-height:17px}
.social{position:absolute;left:552px;top:9px;width:210px}
.social h4{text-align:right;font-family:"Raleway",sans-serif;font-weight:400;font-size:21px;color:#555}
.social-rule{height:1px;background:#ccc;margin:8px 0 0}
.social-list{display:flex;justify-content:space-between;margin-top:12px;padding-left:25px}
.social-item{width:55px;text-align:center;font-size:10.5px;color:var(--navy)}
.social-item svg{display:block;margin:0 auto 8px}
.social-item span{display:block;border-top:1px solid var(--navy);padding-top:4px}
.foot-rule{position:absolute;left:101px;top:140px;width:661px;height:1px;background:#d8d8d8}
.copyright{position:absolute;right:101px;top:150px;font-size:10px;color:#888}
</style>
</head>
<body>
<div class="top-strip"></div>

<header class="site-header">
  <a class="brand" href="#"><span class="brand-dot"></span><span class="brand-name">Pim Sa Ox</span></a>
  <p class="brand-claim">#1 Video Classifieds</p>
  <a class="btn btn-create" href="#">Create an ad</a>
  <a class="btn btn-signin" href="#">Sign in</a>
  <div class="search">Search<span class="search-go">Go</span></div>
  <div class="lang">English</div>
</header>

<nav class="main-nav">
  <div class="nav-bar">
    <a class="nav-item" style="width:74px" href="#">CARS
      <svg class="nav-icon" width="22" height="18" viewBox="0 0 22 18"><path d="M4 8 6 3h10l2 5h2v6h-3v3h-3v-3H8v3H5v-3H2V8z" fill="#fff"/><circle cx="6" cy="11" r="1.5" fill="#0d4a86"/><circle cx="16" cy="11" r="1.5" fill="#0d4a86"/></svg></a>
    <a class="nav-item" style="width:78px" href="#">BOATS
      <svg class="nav-icon" width="22" height="20" viewBox="0 0 22 20"><path d="M8 1h6v4H8zM5 6h12v5H5zM1 12h20l-3 6H4z" fill="#fff"/></svg></a>
    <a class="nav-item" style="width:121px" href="#">ELECTRONICS
      <svg class="nav-icon" width="22" height="20" viewBox="0 0 22 20"><path d="M7 1l4 4 4-4" stroke="#fff" fill="none" stroke-width="1.5"/><rect x="1" y="5" width="20" height="14" rx="2" fill="#fff"/><rect x="3" y="7" width="13" height="10" fill="#0d4a86"/></svg></a>
    <a class="nav-item" style="width:116px" href="#">REAL ESTATE
      <svg class="nav-icon" width="22" height="20" viewBox="0 0 22 20"><path d="M11 1 1 10h3v9h5v-6h4v6h5v-9h3z" fill="#fff"/></svg></a>
    <a class="nav-item" style="width:118px" href="#">ROOMMATES
      <svg class="nav-icon" width="22" height="20" viewBox="0 0 22 20"><circle cx="7" cy="5" r="3" fill="#fff"/><circle cx="15" cy="5" r="3" fill="#fff"/><circle cx="11" cy="8" r="3" fill="#fff"/><path d="M3 18v-6c0-2 8-2 8 0v6zM11 18v-6c0-2 8-2 8 0v6z" fill="#fff"/></svg></a>
    <a class="nav-item" style="width:154px" href="#">OTHER CATEGORIES
      <svg class="nav-icon" width="18" height="16" viewBox="0 0 18 16"><path d="M1 6h9V1l7 7-7 7v-5H1z" fill="#fff"/></svg></a>
  </div>
</nav>

<section class="hero">
  <div class="hero-media" role="img" aria-label="Video still of a white and black motor yacht cruising on deep blue water under a bright cloudy sky, passengers relaxing on deck"></div>
  <svg class="play" width="92" height="92" viewBox="0 0 92 92"><circle cx="46" cy="46" r="43" fill="rgba(255,255,255,.18)" stroke="#fff" stroke-width="3"/><path d="M34 26 66 46 34 66z" fill="#fff"/></svg>
</section>
<div class="slider-dots"><span class="active"></span><span></span><span></span><span></span></div>

<section class="featured">
  <p class="featured-kicker">Browse</p>
  <h2 class="featured-title">Featured on Pim Sa Ox</h2>
  <div class="tabs">
    <a class="tab active" style="width:110px" href="#">MOST VIEWED</a>
    <a class="tab" style="width:111px" href="#">MOST RECENT</a>
    <a class="tab" style="width:146px" href="#">MOST INTERESTING</a>
  </div>
  <div class="featured-rule"></div>
  <div class="thumbs">
    <div class="thumb" role="img" aria-label="Video thumbnail: black luxury SUV on a white background" style="background:linear-gradient(170deg,#f4f5f6 0%,#e3e5e8 22%,#2b2e33 40%,#121417 62%,#55585c 80%,#f0f1f2 100%)"></div>
    <div class="thumb" role="img" aria-label="Video thumbnail: white motor yacht on blue water" style="background:linear-gradient(170deg,#4f86c8 0%,#cfdceb 30%,#ffffff 50%,#262a30 62%,#e9edf1 70%,#2c5a8e 100%)"></div>
    <div class="thumb" role="img" aria-label="Video thumbnail: two-storey suburban house with lawn" style="background:linear-gradient(#a9c9ea 0%,#cfd9e0 18%,#b8ae92 35%,#8f8a72 60%,#c6c2b6 75%,#6d9a3e 88%,#4f7a2c 100%)"></div>
    <div class="thumb" role="img" aria-label="Video thumbnail: flat screen TV and home audio set" style="background:linear-gradient(#f2f2f2 0%,#1a1a1a 12%,#0d0d0d 55%,#3a3a3a 70%,#151515 100%)"></div>
    <div class="thumb" role="img" aria-label="Video thumbnail: young person relaxing on a green sofa in a shared room" style="background:linear-gradient(#6b5a44 0%,#9c8a6a 30%,#b9a98a 48%,#7fb03c 65%,#5e8d2a 82%,#2f3a26 100%)"></div>
    <div class="thumb" role="img" aria-label="Video thumbnail: private jet on the tarmac at sunset" style="background:linear-gradient(#6f97c4 0%,#aebfd2 35%,#e6e8ea 52%,#c5a07a 70%,#e4892f 85%,#7a3d14 100%)"></div>
  </div>
</section>

<section class="how">
  <div class="how-rule"></div>
  <h2 class="how-title">HOW IT WORKS</h2>
  <svg class="steps" width="863" height="230" viewBox="0 0 863 230">
    <defs>
      <linearGradient id="step-create" x1="0" y1="0" x2="0" y2="1"><stop offset="0" stop-color="#c9b6a4"/><stop offset=".45" stop-color="#7a5e4e"/><stop offset="1" stop-color="#2f2a28"/></linearGradient>
      <linearGradient id="step-upload" x1="0" y1="0" x2="1" y2="1"><stop offset="0" stop-color="#f6f2ef"/><stop offset=".5" stop-color="#e9a27a"/><stop offset="1" stop-color="#f3ede9"/></linearGradient>
      <linearGradient id="step-sell" x1="0" y1="0" x2="0" y2="1"><stop offset="0" stop-color="#f4eeee"/><stop offset=".5" stop-color="#e24a4a"/><stop offset="1" stop-color="#3fa48a"/></linearGradient>
    </defs>
    <path d="M333 134H349M514 134H530" stroke="#e2461b" stroke-width="1.5"/>
    <circle cx="251" cy="134" r="83" fill="#fff" stroke="#e2461b" stroke-width="1.5"/>
    <circle cx="431" cy="134" r="83" fill="#fff" stroke="#e2461b" stroke-width="1.5"/>
    <circle cx="612" cy="134" r="83" fill="#fff" stroke="#e2461b" stroke-width="1.5"/>
    <circle cx="251" cy="134" r="76" fill="url(#step-create)" role="img" aria-label="Photo of a person holding a vintage camera"/>
    <circle cx="431" cy="134" r="76" fill="url(#step-upload)" role="img" aria-label="Illustration of upward arrows for uploading"/>
    <circle cx="612" cy="134" r="76" fill="url(#step-sell)" role="img" aria-label="Photo of a couple holding a sold sign"/>
  </svg>
  <p class="step-label" style="left:166px">CREATE IT</p>
  <p class="step-label" style="left:346px">UPLOAD IT</p>
  <p class="step-label" style="left:527px">SELL IT</p>
</section>

<footer class="site-footer">
  <div class="foot-col" style="left:101px"><h4>BUY / BROWSE</h4><ul><li>Roommates</li><li>Cars</li><li>Boats</li><li>Electronics</li><li>Others</li></ul></div>
  <div class="foot-col" style="left:212px"><h4>SELL</h4><ul><li>Start Selling</li><li>Login</li><li>Shooting Video</li><li>Uploading Video</li><li>Buying</li></ul></div>
  <div class="foot-col" style="left:318px"><h4>INFO</h4><ul><li>VBlog</li><li>FAQs</li><li>Terms of Use</li><li>Privacy Policy</li><li>Buyer/Seller Safety</li></ul></div>
  <div class="foot-col" style="left:435px"><h4>CONTACT</h4><ul><li>Contact Us</li><li>Feedback Form</li><li>Referral Program</li><li>Business Register</li><li>Subscription</li></ul></div>
  <div class="social">
    <h4>Stay Social</h4>
    <div class="social-rule"></div>
    <div class="social-list">
      <a class="social-item" href="#"><svg width="28" height="28"><circle cx="14" cy="14" r="12" fill="#0d4a86"/></svg><span>Pagebook</span></a>
      <a class="social-item" href="#"><svg width="28" height="28"><rect x="3" y="3" width="22" height="22" fill="#0d4a86"/></svg><span>Chirper</span></a>
      <a class="social-item" href="#"><svg width="28" height="28" viewBox="0 0 26 26"><circle cx="5" cy="21" r="3" fill="#0d4a86"/><path d="M2 11a13 13 0 0 1 13 13M2 3a21 21 0 0 1 21 21" stroke="#0d4a86" stroke-width="4" fill="none"/></svg><span>RSS</span></a>
    </div>
  </div>
  <div class="foot-rule"></div>
  <p class="copyright">© 2011 Pim Sa Ox</p>
</footer>
</body>
</html>
```